Customer Facing Document Design

Looking for professional design in Word for 5 Templates:

- Purchase Contract
- Sales Contract
- Packing List
- Settlement Report
- Invoice

I have attached our current designs and also some example designs that we want to look similar to. We want our company logo included on all documents. On the Purchase Order, Sales Order, Settlement Report, Invoice we also want our PQV accreditation picture and BGRL logo included.

```html
<!DOCTYPE html>
<html lang="en">
<head>
<meta charset="utf-8">
<title>Kestrel Alloys &amp; Metals – Document Templates</title>
<link href="https://fonts.googleapis.com/css2?family=Open+Sans:wght@400;600;700&display=swap" rel="stylesheet">
<style>
:root{
  --canvas:#c8c9cb;
  --paper:#ffffff;
  --ink:#111111;
  --mark:#7a7b7e;
  --link:#2a5fc4;
  --rule:#222222;
  --band:#e6e7e8;
  --badge:#8d8e91;
}
*{box-sizing:border-box;margin:0;padding:0}
html,body{width:1200px;height:2823px;overflow:hidden}
body{background:var(--canvas);font-family:'Open Sans',sans-serif;color:var(--ink);position:relative}
.page{position:absolute;background:var(--paper)}
.abs{position:absolute;white-space:nowrap}
.brand{position:absolute;display:flex;align-items:center;gap:10px;color:var(--mark);font-weight:700}
.brand .dot{border-radius:50%;background:var(--mark);flex:none}
.company{position:absolute;line-height:1.38}
.company b{font-weight:700}
.company a{color:var(--link);text-decoration:underline}
.badges{position:absolute}
.badges .assoc{position:absolute;display:flex;align-items:center;gap:6px;color:var(--badge);font-weight:700}
.badges .assoc i{border-radius:50%;background:var(--badge);display:block}
.badges .seal{position:absolute;border-radius:50%;background:var(--badge)}
.badges .plate{position:absolute;background:var(--badge)}

/* invoice */
.invoice{left:209px;top:101px;width:776px;height:1004px}
.invoice .company{left:507px;top:46px;font-size:15.5px}
.doc-title{font-weight:700}
.meta{position:absolute;font-size:15.5px;line-height:20.5px}
.meta .k{font-weight:700;position:absolute;left:0}
.meta .v{position:absolute}
.inv-table{position:absolute;left:45px;top:455px;width:686px;font-size:14.5px}
.inv-table .head{height:22px;background:var(--band);border-top:3px solid var(--rule);border-bottom:2px solid var(--rule);position:relative;font-weight:700}
.inv-table .row{position:relative;height:49px}
.inv-table .c{position:absolute;top:50%;transform:translateY(-50%);line-height:19px}
.inv-table .end{border-top:3px solid var(--rule)}
.remit{position:absolute;left:45px;top:680px;font-size:13px;line-height:18.5px}

/* settlement & packing */
.report{left:95px;width:1005px;height:776px}
.settlement{top:1135px}
.packing{top:1945px}
.report .company{left:742px;top:63px;font-size:13px;line-height:17.5px}
.small{font-size:12.5px}
.grid{position:absolute;font-size:12px}
.grid .row{position:relative;height:18.3px}
.grid .row.shade{background:var(--band)}
.grid .c{position:absolute;top:50%;transform:translateY(-50%);white-space:nowrap}
.grid .vline{position:absolute;top:0;bottom:0;width:2px;background:var(--paper)}
.r{text-align:right}
.mid{transform:translate(-50%,-50%)!important}
</style>
</head>
<body>

<!-- SALES INVOICE -->
<section class="page invoice">
  <div class="brand" style="left:52px;top:62px;font-size:44px"><span class="dot" style="width:56px;height:56px"></span>KESTREL</div>
  <div class="company">
    <b>KESTREL ALLOYS &amp; METALS</b><br>
    4810 Larkspur Circle,<br>
    Fairview Park. CA 90471<br>
    +44 7700 900418<br>
    <a>sales@kestrel-am.com</a><br>
    <a>www.kestrel-am.com</a>
  </div>

  <h1 class="doc-title abs" style="left:45px;top:221px;font-size:23px">SALES INVOICE</h1>

  <div class="meta" style="left:440px;top:238px;width:330px;height:45px">
    <span class="k" style="top:0">Contract No</span><span class="v" style="left:125px;top:0">: Northgate 050725</span>
    <span class="k" style="top:21px">Order No</span><span class="v" style="left:125px;top:21px">: P.O. 13222</span>
  </div>

  <div class="meta" style="left:45px;top:295px;width:300px">
    <b>Customer:</b><br>
    <b>NORTHGATE METAL SERVICES</b><br>
    2270 Lakeview Ave<br>
    Cleveland<br>
    OH 44109
  </div>

  <div class="meta" style="left:440px;top:302px;width:330px;height:110px">
    <span class="k" style="top:0">Date</span><span class="v" style="left:125px;top:0">: September 22, 2025</span>
    <span class="k" style="top:20.5px">Delivery</span><span class="v" style="left:125px;top:20.5px">: September 22, 2025</span>
    <span class="k" style="top:41px">Payment</span><span class="v" style="left:125px;top:41px">: On receipt of invoice</span>
    <span class="k" style="top:61.5px">Freight Terms</span><span class="v" style="left:125px;top:61.5px">: FOB Destination</span>
    <span class="k" style="top:82px">Terms</span><span class="v" style="left:125px;top:82px">: Prepaid</span>
  </div>

  <div class="inv-table">
    <div class="head">
      <span class="c" style="left:10px">Item</span>
      <span class="c" style="left:147px">Description</span>
      <span class="c r" style="right:268px">Lbs weight</span>
      <span class="c" style="left:478px">$/lb</span>
      <span class="c r" style="right:7px">Total</span>
    </div>
    <div class="row"><span class="c" style="left:22px">1</span><span class="c" style="left:60px">Solids suitable for sorting &amp; prep to<br>vac Qty – 15,000 to 20,000 Lbs</span><span class="c" style="right:270px">20,000</span><span class="c" style="left:466px">$5.50</span><span class="c" style="right:7px">$110,000.00</span></div>
    <div class="row"><span class="c" style="left:22px">2</span><span class="c" style="left:60px">Solids suitable for sorting &amp; prep to<br>vac Qty – 15,000 to 20,000 Lbs</span><span class="c" style="right:270px">12,000</span><span class="c" style="left:466px">$1.00</span><span class="c" style="right:7px">$12,000.00</span></div>
    <div class="row"><span class="c" style="left:22px">3</span><span class="c" style="left:60px">Solids suitable for sorting &amp; prep to<br>vac Qty – 15,000 to 20,000 Lbs</span><span class="c" style="right:270px">12,000</span><span class="c" style="left:466px">$1.00</span><span class="c" style="right:7px">$12,000.00</span></div>
    <div class="row end" style="height:44px"><span class="c" style="left:384px;font-weight:700">Total</span><span class="c" style="right:7px;font-weight:700">$134,000.00</span></div>
  </div>

  <div class="remit">
    <b>REMIT TO:</b><br>
    Payment by ACH<br>
    Routing Number: 410 736 218<br>
    Account Number: 052 918 4407<br>
    Bank: The Harbor Bank Company
  </div>

  <div class="badges" style="left:405px;top:848px;width:325px;height:90px">
    <div class="assoc" style="left:0;top:44px;font-size:28px"><span>BGRL</span><i style="width:32px;height:32px"></i></div>
    <div class="seal" style="left:164px;top:0;width:60px;height:60px"></div>
    <div class="plate" style="left:164px;top:68px;width:60px;height:12px"></div>
    <div class="plate" style="left:232px;top:4px;width:88px;height:76px"></div>
  </div>
</section>

<!-- SETTLEMENT REPORT -->
<section class="page report settlement">
  <div class="brand" style="left:74px;top:92px;font-size:38px"><span class="dot" style="width:48px;height:48px"></span>KESTREL</div>
  <div class="company">
    <b>KESTREL ALLOYS &amp; METALS</b><br>
    4810 Larkspur Circle,<br>
    Fairview Park. CA 90471<br>
    +44 7700 900418<br>
    <a>sales@kestrel-am.com</a><br>
    <a>www.kestrel-am.com</a>
  </div>

  <h1 class="doc-title abs" style="left:92px;top:184px;font-size:18.5px">SETTLEMENT REPORT</h1>

  <div class="abs small" style="left:92px;top:227px;line-height:17.5px">SUPPLIER: BRIGHTSIDE RECYCLING<br>Lot No: 877<br>PO No.:</div>
  <div class="abs small" style="left:684px;top:227px;line-height:17.5px">DATE<br>RECEIVING DATE</div>
  <div class="abs small" style="left:799px;top:227px;line-height:17.5px">: September 19, 2025<br>: August 11, 2025</div>

  <div class="grid" style="left:80px;top:366px;width:845px;border-top:2px solid var(--rule)">
    <div class="row" style="height:37px;border-bottom:2px solid var(--rule);font-weight:700;font-size:11.5px">
      <span class="c mid" style="left:25px">Item</span>
      <span class="c mid" style="left:112px">Advised as</span>
      <span class="c mid" style="left:279px">Graded as</span>
      <span class="c mid" style="left:425px;text-align:center;line-height:15px">Advised<br>(lbs)</span>
      <span class="c mid" style="left:505px;text-align:center;line-height:15px">Received<br>(lbs)</span>
      <span class="c mid" style="left:654px">$/lb</span>
      <span class="c mid" style="left:747px">Total</span>
    </div>
    <div class="row shade"><i class="vline" style="left:50px"></i><i class="vline" style="left:170px"></i><i class="vline" style="left:370px"></i><i class="vline" style="left:444px"></i><i class="vline" style="left:530px"></i><span class="c mid" style="left:25px">1</span><span class="c" style="left:63px">Ni 718 Turnings</span><span class="c" style="left:177px">Ni 718 Turnings - 1% Alum 1% Fe</span><span class="c mid" style="left:505px">284</span><span class="c" style="right:202px">$5.2000</span><span class="c" style="right:8px">$1,476.80</span></div>
    <div class="row"><span class="c mid" style="left:25px">2</span><span class="c" style="left:177px">Ni 718 Turnings - 1% Alum 1% Fe</span><span class="c mid" style="left:505px">1382</span><span class="c" style="right:202px">$5.2000</span><span class="c" style="right:8px">$7,186.40</span></div>
    <div class="row shade"><i class="vline" style="left:50px"></i><i class="vline" style="left:170px"></i><i class="vline" style="left:370px"></i><i class="vline" style="left:444px"></i><i class="vline" style="left:530px"></i><span class="c mid" style="left:25px">3</span><span class="c" style="left:177px">Ni 718 Turnings - 1% Alum 1% Fe</span><span class="c mid" style="left:505px">1390</span><span class="c" style="right:202px">$5.2000</span><span class="c" style="right:8px">$7,228.00</span></div>
    <div class="row"><span class="c mid" style="left:25px">4</span><span class="c" style="left:177px">Steel Turnings</span><span class="c mid" style="left:505px">556</span><span class="c" style="right:202px">$5.2000</span><span class="c" style="right:8px">$0.00</span></div>
    <div class="row shade"><i class="vline" style="left:50px"></i><i class="vline" style="left:170px"></i><i class="vline" style="left:370px"></i><i class="vline" style="left:444px"></i><i class="vline" style="left:530px"></i><span class="c mid" style="left:25px">5</span><span class="c" style="left:177px">Ni 718 Turnings - 1% Alum 1% Fe</span><span class="c mid" style="left:505px">1340</span><span class="c" style="right:202px">$5.2000</span><span class="c" style="right:8px">$6,968.00</span></div>
    <div class="row"><span class="c mid" style="left:25px">6</span><span class="c" style="left:177px">Ni 718 Turnings - 1% Alum 1% Fe</span><span class="c mid" style="left:505px">1528</span><span class="c" style="right:202px">$5.2000</span><span class="c" style="right:8px">$7,945.60</span></div>
    <div class="row shade" style="border-bottom:2px solid var(--rule)"><i class="vline" style="left:50px"></i><i class="vline" style="left:170px"></i><i class="vline" style="left:370px"></i><i class="vline" style="left:444px"></i><i class="vline" style="left:530px"></i></div>
    <div class="row" style="height:24px;font-weight:700;font-size:15.5px"><span class="c" style="right:192px">Total</span><span class="c" style="right:8px">$30,804.80</span></div>
  </div>

  <div class="badges" style="left:618px;top:655px;width:310px;height:64px">
    <div class="assoc" style="left:0;top:14px;font-size:30px"><span>BGRL</span><i style="width:34px;height:34px"></i></div>
    <div class="seal" style="left:182px;top:0;width:46px;height:46px"></div>
    <div class="plate" style="left:182px;top:52px;width:46px;height:10px"></div>
    <div class="plate" style="left:234px;top:2px;width:70px;height:58px"></div>
  </div>
</section>

<!-- PACKING LIST -->
<section class="page report packing">
  <div class="brand" style="left:74px;top:68px;font-size:32px"><span class="dot" style="width:42px;height:42px"></span>KESTREL</div>
  <div class="company">
    <b>KESTREL ALLOYS &amp; METALS</b><br>
    4810 Larkspur Circle,<br>
    Fairview Park. CA 90471<br>
    +44 7700 900418<br>
    <a>sales@kestrel-am.com</a><br>
    <a>www.kestrel-am.com</a>
  </div>

  <h1 class="doc-title abs" style="left:92px;top:167px;font-size:18.5px">PACKING LIST</h1>

  <div class="abs" style="left:92px;top:210px;font-size:12px;line-height:17.5px"><b>SHIP TO:</b><br><b>Ridgeline Alloys Ltd</b><br>12 Millbrook Works, Hollow Road<br>Darnall, Sheffield S9 4QT</div>

  <div class="abs" style="left:669px;top:182px;font-size:12px;line-height:17px;font-weight:700">BOL#<br>PO#<br>Date<br>Via<br>FOB<br>Sales Order</div>
  <div class="abs" style="left:785px;top:182px;font-size:12px;line-height:17px;font-weight:700">:<br>:&nbsp;&nbsp;0<br>:&nbsp;&nbsp;9/29/25<br>:&nbsp;&nbsp;Curtain Sider<br>:&nbsp;&nbsp;Destination<br>:</div>

  <div class="grid" style="left:88px;top:289px;width:829px;border-top:2px solid var(--rule)">
    <div class="row" style="height:18px;border-bottom:1px solid var(--rule);font-weight:700">
      <span class="c mid" style="left:43px">Box</span><span class="c mid" style="left:159px">Material</span><span class="c mid" style="left:314px">Packages</span><span class="c mid" style="left:463px">Gross (lbs)</span><span class="c mid" style="left:592px">Tare (lbs)</span><span class="c mid" style="left:733px">Net</span>
    </div>
    <div class="row shade"><i class="vline" style="left:85px"></i><i class="vline" style="left:245px"></i><i class="vline" style="left:383px"></i><i class="vline" style="left:544px"></i><i class="vline" style="left:641px"></i><span class="c mid" style="left:43px">031925/03</span><span class="c" style="left:93px">Ni 718 Turnings</span><span class="c mid" style="left:314px">bag inside stillage</span><span class="c" style="right:293px">303</span><span class="c" style="right:197px">50</span><span class="c" style="right:8px">253</span></div>
    <div class="row"><span class="c mid" style="left:43px">031925/04</span><span class="c" style="left:93px">Ni 718 Turnings</span><span class="c mid" style="left:314px">stillage</span><span class="c" style="right:293px">461</span><span class="c" style="right:197px">55</span><span class="c" style="right:8px">406</span></div>
    <div class="row shade"><i class="vline" style="left:85px"></i><i class="vline" style="left:245px"></i><i class="vline" style="left:383px"></i><i class="vline" style="left:544px"></i><i class="vline" style="left:641px"></i><span class="c mid" style="left:43px">031925/05</span><span class="c" style="left:93px">Ni 718 Turnings</span><span class="c mid" style="left:314px">stillage</span><span class="c" style="right:293px">242</span><span class="c" style="right:197px">51</span><span class="c" style="right:8px">191</span></div>
    <div class="row"><span class="c mid" style="left:43px">031925/06</span><span class="c" style="left:93px">Ni 718 Turnings</span><span class="c mid" style="left:314px">stillage</span><span class="c" style="right:293px">769</span><span class="c" style="right:197px">54</span><span class="c" style="right:8px">715</span></div>
    <div class="row shade"><i class="vline" style="left:85px"></i><i class="vline" style="left:245px"></i><i class="vline" style="left:383px"></i><i class="vline" style="left:544px"></i><i class="vline" style="left:641px"></i><span class="c mid" style="left:43px">031925/07</span><span class="c" style="left:93px">Ni 718 Turnings</span><span class="c mid" style="left:314px">stillage</span><span class="c" style="right:293px">281</span><span class="c" style="right:197px">45</span><span class="c" style="right:8px">236</span></div>
    <div class="row"><span class="c mid" style="left:43px">031925/08</span><span class="c" style="left:93px">Ni 718 Turnings</span><span class="c mid" style="left:314px">stillage</span><span class="c" style="right:293px">473</span><span class="c" style="right:197px">49</span><span class="c" style="right:8px">424</span></div>
    <div class="row shade"><i class="vline" style="left:85px"></i><i class="vline" style="left:245px"></i><i class="vline" style="left:383px"></i><i class="vline" style="left:544px"></i><i class="vline" style="left:641px"></i><span class="c mid" style="left:43px">031925/09</span><span class="c" style="left:93px">Ni 718 Turnings</span><span class="c mid" style="left:314px">stillage</span><span class="c" style="right:293px">698</span><span class="c" style="right:197px">52</span><span class="c" style="right:8px">646</span></div>
    <div class="row" style="height:18px"></div>
    <div class="row shade"><i class="vline" style="left:85px"></i><i class="vline" style="left:245px"></i><i class="vline" style="left:383px"></i><i class="vline" style="left:544px"></i><i class="vline" style="left:641px"></i></div>
    <div class="row" style="height:18px"></div>
    <div class="row shade"><i class="vline" style="left:85px"></i><i class="vline" style="left:245px"></i><i class="vline" style="left:383px"></i><i class="vline" style="left:544px"></i><i class="vline" style="left:641px"></i></div>
    <div class="row" style="height:18px"></div>
    <div class="row shade"><i class="vline" style="left:85px"></i><i class="vline" style="left:245px"></i><i class="vline" style="left:383px"></i><i class="vline" style="left:544px"></i><i class="vline" style="left:641px"></i></div>
    <div class="row" style="height:18px"></div>
    <div class="row shade"><i class="vline" style="left:85px"></i><i class="vline" style="left:245px"></i><i class="vline" style="left:383px"></i><i class="vline" style="left:544px"></i><i class="vline" style="left:641px"></i></div>
    <div class="row" style="height:19px"></div>
    <div class="row shade" style="font-weight:700;font-size:12.5px"><i class="vline" style="left:85px"></i><i class="vline" style="left:245px"></i><i class="vline" style="left:383px"></i><i class="vline" style="left:544px"></i><i class="vline" style="left:641px"></i><span class="c" style="right:453px">Total</span><span class="c" style="right:293px">7,724</span><span class="c" style="right:197px">990</span><span class="c" style="right:8px">6,734</span></div>
  </div>

  <div class="badges" style="left:693px;top:671px;width:230px;height:50px">
    <div class="assoc" style="left:0;top:16px;font-size:21px"><span>BGRL</span><i style="width:24px;height:24px"></i></div>
    <div class="seal" style="left:135px;top:0;width:34px;height:34px"></div>
    <div class="plate" style="left:135px;top:38px;width:34px;height:8px"></div>
    <div class="plate" style="left:175px;top:2px;width:51px;height:44px"></div>
  </div>
</section>

</body>
</html>
```